Tobias Wrenfield - Cinematographer

NEED:
I'm looking for a sleek, professional, modern business card that will give give the recipient the impression that they can trust their production will go smoothly by hiring me. I will bring creativity and knowledge to their shoot, so that we can create powerful images.
I am looking for a card with a strong style and design ethos that could be expanded to a website and a full visual/graphic/design entity for me.
ABOUT ME:
I am a mid-twenties cinematographer, I work on music video, narrative short, commercial, and corporate projects. I blend the science and artistry of cameras and filmmaking to tell a story. I'm an artist, a technician, and a manager.
DESIGN:
I like sleek, simple design. Black, dark grays, white, dark navy, steel blues, I love cyan, but also cyan and red. I am not a fan of earthy tones. I generally prefer modern, san-serif fonts over serifs. My old logo was based on an aperture, a multi-blade device at the back of a lens that controls how much light passes through, but I made it with so many colors, that it doesn't necessarily lend itself to a specific color-scheme or design ethos. I liked that the aperture design provided a sense of the technical requirements of my job. I'm a fan of matte business cards, but am open to plenty of specialty print processes to make an outstanding card.
ATTACHED FILES:
My Old Rainbox Aperture Logo, plus a few designs I've tried playing around with, but am not tied to. I AM OPEN TO NEW DESIGNS, DO NOT FEEL TIED TO THIS.
**I've pulled my old logo down from the attached files, and instead attached other business cards I like, so as not to mislead you where I would like to go.
INFO:
Name: Tobias Wrenfield
Job: Cinematographer
Email: tkwrenfield@quillbox.example
Phone: 503.618.2907
Website: tobiaswrenfield.example
Updates
I'm adding some images of other cards that I like, and removing my old logo, since I'm looking for something new, and don't want that old logo to push anyone a certain direction.

```html
<!DOCTYPE html>
<html lang="en">
<head>
<meta charset="utf-8">
<title>Tobias Wrenfield – Cinematographer Cards</title>
<link rel="stylesheet" href="https://fonts.googleapis.com/css2?family=Lato:wght@400;700&display=swap">
<style>
  :root {
    --page: #ffffff;
    --ink: #111111;
    --rim-dark: #2b2b2b;
    --rule: #b5b5b5;
    --wedge-light: #d5d5d5;
    --card-light: #ffffff;
    --card-dark: #000000;
    --wedge-dark: #3a3a3a;
    --rule-dark: #6f6f6f;
    --title-gray: #7a7a7a;
    --white: #ffffff;
  }
  html, body {
    margin: 0;
    padding: 0;
    width: 1200px;
    height: 1038px;
    overflow: hidden;
    background: var(--page);
  }
  .canvas { display: block; width: 1200px; height: 1038px; }
  .name {
    font-family: "Lato", sans-serif;
    font-weight: 700;
    font-size: 31px;
  }
  .title {
    font-family: "Lato", sans-serif;
    font-weight: 400;
    font-size: 18px;
    letter-spacing: 5.6px;
    fill: var(--title-gray);
  }
  .contact {
    font-family: "Lato", sans-serif;
    font-weight: 400;
    font-size: 11.5px;
    fill: var(--white);
  }
  .card-front .name { fill: var(--ink); }
  .card-back .name { fill: var(--white); }
</style>
</head>
<body>
<svg class="canvas" viewBox="0 0 1200 1038" xmlns="http://www.w3.org/2000/svg">
  <defs>
    <filter id="card-shadow" x="-10%" y="-10%" width="120%" height="120%">
      <feDropShadow dx="0" dy="2" stdDeviation="3" flood-color="#000" flood-opacity="0.35"/>
    </filter>
    <filter id="name-glow" x="-10%" y="-30%" width="120%" height="160%">
      <feGaussianBlur stdDeviation="2.2" result="blur"/>
      <feMerge><feMergeNode in="blur"/><feMergeNode in="SourceGraphic"/></feMerge>
    </filter>
  </defs>

  <g class="card-front" transform="translate(270 270)">
    <circle r="204" fill="var(--card-light)" stroke="var(--rim-dark)" stroke-width="7" filter="url(#card-shadow)"/>
    <path d="M0 0 L0 -200 A200 200 0 0 0 -147 136 Z" fill="var(--wedge-light)"/>
    <circle r="185" fill="none" stroke="var(--rule)" stroke-width="3"/>
    <line x1="0" y1="-200" x2="0" y2="200" stroke="var(--rule)" stroke-width="2.5"/>
    <line x1="-186" y1="-6" x2="186" y2="-6" stroke="var(--rule)" stroke-width="2.5"/>
    <text class="name" x="-167" y="-21">TOBIAS WRENFIELD</text>
    <text class="title" x="-110" y="17">CINEMATOGRAPHER</text>
  </g>

  <g class="card-back" transform="translate(270 770)">
    <circle r="206" fill="var(--white)" filter="url(#card-shadow)"/>
    <circle r="198" fill="var(--card-dark)"/>
    <path d="M0 0 L0 -198 A198 198 0 0 0 -144 136 Z" fill="var(--wedge-dark)"/>
    <circle r="184" fill="none" stroke="var(--rule-dark)" stroke-width="2.5"/>
    <line x1="0" y1="-198" x2="0" y2="198" stroke="var(--rule-dark)" stroke-width="2"/>
    <line x1="-186" y1="-13" x2="186" y2="-13" stroke="var(--rule-dark)" stroke-width="2"/>
    <text class="name" x="-167" y="-28" filter="url(#name-glow)">TOBIAS WRENFIELD</text>
    <text class="title" x="-110" y="10">CINEMATOGRAPHER</text>
    <text class="contact" x="9" y="41">503.618.2907</text>
    <text class="contact" x="9" y="61">tkwrenfield@quillbox.example</text>
    <text class="contact" x="9" y="80">www.tobiaswrenfield.example</text>
  </g>
</svg>
</body>
</html>
```